Building technology company seek stationery design and folder design

Letterhead, and a folder design
ideally, I would have two letter head design, one is for one-page bussiness letter. the other one I can use for longer document such report, or analysis regular report page
you can find company logo and overall style at our website:
www.plinthcove.example

we are in building technology business, using internet of things technology to improve building energy efficiency to make building greener.

Industry/Entity Type

It Company

Requirements
Must have
• company logo
Nice to have
• techy look abstract graphics, etc.
Should not have
• no comment

```html
<!DOCTYPE html>
<html lang="en">
<head>
<meta charset="utf-8">
<title>Plinth Cove — Presentation Folder</title>
<link rel="stylesheet" href="https://fonts.googleapis.com/css2?family=Montserrat:wght@400;500&display=swap">
<style>
  :root {
    --stage: #d6d6d6;
    --ink-dark: #0b1e1f;
    --ink-faint: #142a29;
    --lime: #a4c93b;
    --stone: #807e6e;
    --paper: #ffffff;
    --logo-grey: #6f7065;
    --text-light: #e6e8e2;
  }
  * { margin: 0; padding: 0; box-sizing: border-box; }
  html, body { width: 1200px; height: 847px; overflow: hidden; }
  body {
    background: var(--stage);
    font-family: "Montserrat", sans-serif;
    position: relative;
  }
  .folder {
    position: absolute;
    left: 80px; top: 56px;
    width: 1040px; height: 735px;
    display: flex;
  }
  .panel { position: relative; width: 520px; height: 735px; overflow: hidden; }

  /* Back cover */
  .back-cover { background: var(--ink-dark); }
  .back-cover .faint-mark {
    position: absolute; left: 150px; top: 420px;
    width: 300px; height: 190px;
    background: var(--ink-faint);
  }
  .back-cover .rule {
    position: absolute; left: 0; right: 0; top: 660px;
    height: 3px; background: var(--lime);
  }
  .back-cover .brand {
    position: absolute; left: 36px; top: 628px;
    display: flex; align-items: center; gap: 10px;
  }
  .brand-square { width: 22px; height: 22px; background: var(--lime); }
  .back-cover .brand-name {
    font-size: 19px; letter-spacing: 1.5px; color: var(--logo-grey);
    text-transform: uppercase; font-weight: 400;
  }
  .contact {
    position: absolute; left: 300px; top: 612px;
    font-size: 8px; line-height: 13px; color: var(--text-light);
  }
  .contact-row { display: flex; align-items: center; gap: 5px; }
  .contact-row svg { width: 8px; height: 8px; }
  .social {
    position: absolute; left: 410px; top: 614px;
    display: flex; gap: 6px;
  }
  .social span {
    width: 11px; height: 11px; border-radius: 50%;
    border: 1px solid var(--text-light);
  }

  /* Front cover */
  .front-cover { background: var(--ink-dark); }
  .front-cover .masthead {
    position: absolute; left: 0; top: 0; width: 100%; height: 178px;
    background: var(--paper);
    display: flex; align-items: center; justify-content: center; gap: 10px;
  }
  .front-cover .brand-name {
    font-size: 17px; letter-spacing: 1.5px; color: var(--logo-grey);
    text-transform: uppercase;
  }
  .front-cover .lime-band {
    position: absolute; left: 0; top: 178px; width: 100%; height: 9px;
    background: var(--lime);
  }
  .front-cover .hero-mark {
    position: absolute; left: 60px; top: 250px;
    width: 460px; height: 360px;
    background: linear-gradient(135deg, var(--lime) 0%, var(--lime) 60%, #8fb236 100%);
  }
  .front-cover .footer-band {
    position: absolute; left: 0; bottom: 0; width: 100%; height: 125px;
    background: var(--stone);
    display: flex; align-items: center; justify-content: center;
  }
  .front-cover .web {
    font-size: 10px; color: var(--text-light); letter-spacing: 0.5px;
  }
</style>
</head>
<body>
  <main class="folder">
    <section class="panel back-cover">
      <div class="faint-mark" role="img" aria-label="Faint large brand mark decoration"></div>
      <div class="contact">
        <div class="contact-row">
          <svg viewBox="0 0 10 10"><circle cx="5" cy="5" r="5" fill="#a4c93b"/></svg>
          <span>(555) 014-2290</span>
        </div>
        <div class="contact-row">
          <svg viewBox="0 0 10 10"><circle cx="5" cy="5" r="5" fill="#a4c93b"/></svg>
          <span>info@plinthcove.example</span>
        </div>
      </div>
      <div class="social" aria-hidden="true"><span></span><span></span><span></span><span></span></div>
      <div class="brand">
        <div class="brand-square"></div>
        <span class="brand-name">Plinth Cove</span>
      </div>
      <div class="rule"></div>
    </section>

    <section class="panel front-cover">
      <header class="masthead">
        <div class="brand-square"></div>
        <span class="brand-name">Plinth Cove</span>
      </header>
      <div class="lime-band"></div>
      <div class="hero-mark" role="img" aria-label="Large brand mark decoration in lime green"></div>
      <footer class="footer-band">
        <span class="web">www.plinthcove.example</span>
      </footer>
    </section>
  </main>
</body>
</html>
```